New Web Site For New Company

We need a website for a new venture.

Our existing site can be found at:

www.qvrn.co.uk

Content and text can be taken from there.

As the new logo suggests we do not like formal websites, template website. We like to be a bit different.

We are looking for:

Edgy
Clean
Easy to navigate
Fun
Memorable

PAGE HEADINGS:

HOME
CONSTRUCTION (3 Pages) - Portable Toilets
- Towable Welfare (like that can be found at yarrowpods.co.uk)
- Temporary Fencing

EVENTS (One Page)

ABOUT US (With .pdf downloads)

CONTACT US - FORM

We see the front page as basic with not lots of text just a basic introduction for SEO purposes that does not allow people to get bogged down with and actively encourages them to go further into the site.

As the logo suggests. We like illustrations like our logo shows. We want to keep photos of product off the front page and in other sections.

Our current site (www.qvrn.co.uk) achieves this via a video. I do not want to go this route this time.

Simple and Clean is the key.

The over sections can be lifted from the existing site. More of a make over.

This is a new start hence new style.
Updates

We have had a chat internally and we like:

http://www.brimtallow.com

Something like this could work very well

Industry/Entity Type

Construction

Colors
acd036

```html
<!DOCTYPE html>
<html lang="en">
<head>
<meta charset="utf-8">
<title>Hartwell Loo Hire</title>
<link href="https://fonts.googleapis.com/css2?family=Archivo:wght@700;800;900&family=PT+Sans:wght@400;700&family=Open+Sans:wght@400;600&display=swap" rel="stylesheet">
<style>
:root{
  --green:#6e9a22;
  --green-dark:#4f7a14;
  --green-light:#8dbb3a;
  --page:#f8fafa;
  --heading:#454545;
  --body:#555;
  --muted:#9a9a9a;
  --footer:#43484b;
  --footer-dark:#2f3335;
  --footer-text:#e8e8e8;
  --rule:#5d6366;
}
*{box-sizing:border-box;margin:0;padding:0}
html,body{width:1078px;height:1200px;overflow:hidden}
body{background:var(--page);font-family:"PT Sans",sans-serif;color:var(--body);position:relative}
.abs{position:absolute}
.logo-art{left:130px;top:8px;width:168px;height:110px;background:radial-gradient(circle at 60% 40%,#a9d04a,#3d7fc0 70%,#e9eeea 100%);border-radius:4px}
.brand{left:298px;top:62px;font-family:"Archivo",sans-serif;font-weight:800;font-size:21px;color:var(--green)}
.social-top{right:145px;top:13px;display:flex;gap:8px}
.sq{width:29px;height:29px;border-radius:3px;background:#5f6f7a}
.call{right:145px;top:60px;font-family:"Archivo",sans-serif;font-weight:700;font-size:14.5px;color:#8a8a8a;display:flex;align-items:center;gap:5px}
.call b{color:var(--green)}
.call svg{width:20px;height:20px}
.nav{left:143px;top:125px;width:793px;height:43px;background:linear-gradient(#80ac30,#5d8a1a);border:1px solid var(--green-dark);border-radius:2px;display:flex;align-items:center;justify-content:space-around;padding:0 20px}
.nav a{font-family:"Archivo",sans-serif;font-weight:800;font-size:14px;letter-spacing:.8px;color:#e3efcc;text-decoration:none;text-shadow:0 1px 1px #3b5c0c}
.nav a.active{color:#fff}
.hero{left:141px;top:184px;width:795px;height:316px;background:linear-gradient(180deg,#e9ecea 0%,#d5dad6 45%,#7f9a6e 78%,#6f8f4b 100%)}
.hero-product{left:220px;top:200px;width:175px;height:275px;border-radius:30px 30px 6px 6px;background:linear-gradient(90deg,#1d4fc7,#2f6ef0 50%,#1a46b0)}
.hero-title{left:484px;top:262px;width:420px;font-family:"Archivo",sans-serif;font-weight:800;font-size:25.5px;line-height:30px;color:var(--heading)}
.btn{left:481px;top:378px;width:117px;height:37px;background:linear-gradient(#86b43a,#5f8e1d);border:1px solid #a7cc63;border-radius:2px;color:#fff;font-family:"Archivo",sans-serif;font-weight:800;font-size:12.5px;display:flex;align-items:center;justify-content:center;text-shadow:0 1px 1px #3b5c0c}
.clients{left:139px;top:500px;width:797px;height:47px;background:#ececec;display:flex;align-items:center;gap:26px;padding-left:105px;font-family:"Archivo",sans-serif;font-weight:800;color:#b9b9b9;white-space:nowrap}
.clients .label{font-size:15px}
.clients span{font-size:14px}
.about-photo{left:135px;top:642px;width:165px;height:165px;border-radius:50%;background:linear-gradient(180deg,#8e8672 0%,#9aa0a1 45%,#7a8b5b 80%,#6f8a3f 100%)}
.sec-h{font-family:"Archivo",sans-serif;font-weight:800;font-size:13.5px;letter-spacing:.8px;color:var(--heading)}
.intro{left:325px;top:643px;width:335px}
.intro p{font-size:10.5px;line-height:15.2px;margin-top:18px}
.intro p.lead{font-weight:700;margin-top:18px}
.updates{left:683px;top:642px;width:255px}
.updates h3{font-family:"PT Sans",sans-serif;font-weight:400;font-size:15px;color:var(--green);margin-top:17px}
.updates p{font-size:9.6px;line-height:15.2px;font-weight:700;color:#666;margin-top:6px}
.updates .date{font-size:8.5px;color:#888;margin-top:12px;display:flex;gap:4px;align-items:center}
.footer{left:0;top:892px;width:1078px;height:270px;background:linear-gradient(#4b5053,#3a3e41);border-top:2px solid #393c3e;font-family:"Open Sans",sans-serif;color:var(--footer-text)}
.fcol{position:absolute;top:45px}
.fcol h4{font-size:13.5px;font-weight:600;color:#fff;padding-bottom:6px;border-bottom:1px solid var(--rule);display:flex;justify-content:space-between;align-items:center}
.fcol h4 svg{width:14px;height:14px}
.fcol p{font-size:10.8px;line-height:15.2px;margin-top:12px}
.contact-list{list-style:none;margin-top:18px}
.contact-list li{display:flex;align-items:center;gap:15px;font-size:10.8px;height:25px}
.contact-list svg{width:16px;height:16px}
.signup{display:flex;margin-top:14px;width:252px;height:32px;border:1px solid #6f777b}
.signup .field{flex:1;background:#858e94}
.signup .go{width:67px;background:linear-gradient(#5a6a88,#445470);color:#fff;font-size:10.5px;font-weight:600;display:flex;align-items:center;justify-content:center}
.get-social{font-size:13.5px;font-weight:600;color:#fff;margin-top:22px}
.social-foot{display:flex;gap:10px;margin-top:12px}
.social-foot .sq{width:28px;height:28px;background:#68737a}
.bar{left:0;top:1162px;width:1078px;height:38px;background:linear-gradient(#6e9d25,#4b7a12);color:#fff;font-family:"Open Sans",sans-serif;font-size:9px}
.bar .copy{position:absolute;left:143px;top:12px}
.bar .links{position:absolute;left:830px;top:12px;display:flex;gap:10px}
</style>
</head>
<body>
<header>
  <div class="abs logo-art" role="img" aria-label="Illustrated portable cabin under a green tree"></div>
  <div class="abs brand">Hartwell Loo Hire</div>
  <div class="abs social-top" aria-label="Social links"><div class="sq"></div><div class="sq"></div><div class="sq"></div></div>
  <div class="abs call">
    <svg viewBox="0 0 20 20"><rect width="20" height="20" rx="3" fill="#6e9a22"/><path d="M6 4c1 0 2 2 2 3s-1 1-1 2 2 3 3 3 1-1 2-1 3 1 3 2-1 2-3 2C8 15 5 12 5 7c0-2 0-3 1-3z" fill="#fff"/></svg>
    Call us today <b>+1800.555.0142</b>
  </div>
  <nav class="abs nav">
    <a class="active" href="#">HOME</a><a href="#">CONSTRUCTION</a><a href="#">EVENTS</a><a href="#">ABOUT US</a><a href="#">CONTACT US</a>
  </nav>
</header>

<section>
  <div class="abs hero" role="img" aria-label="Blurred construction site with rows of portable toilets"></div>
  <div class="abs hero-product" role="img" aria-label="Blue portable toilet unit"></div>
  <h1 class="abs hero-title">Reliable Portable Toilets for Construction and Events</h1>
  <div class="abs btn">Learn More</div>
  <div class="abs clients">
    <span class="label">Featured Clients</span>
    <span>Larkfield Media</span><span>Orwin Build</span><span>Trackline Co</span><span>Borough of Elmbrook</span>
  </div>
</section>

<section>
  <div class="abs about-photo" role="img" aria-label="Row of grey portable toilets on grass"></div>
  <div class="abs intro">
    <h2 class="sec-h">THE PORTABLE TOILET HIRE EXPERTS</h2>
    <p class="lead">The Yard Comfort Company was founded in 2006 by its directors Dorian and Felix as a specialist provider of portable toilet hire and sanitation services to the construction and events industries.</p>
    <p>With the ability to provide all of your sanitation solutions, a friendly and knowledgeable staff base, competitive pricing, and a high attention to detail, we are one of the UK's leading providers of portable sanitation equipment and services.</p>
  </div>
  <div class="abs updates">
    <h2 class="sec-h">LATEST UPDATES</h2>
    <h3>The Top 10 Best Consulting Companies</h3>
    <p>The point of using Lorem Ipsum is that it has a more-or-less normal distribution of letters, as opposed to using 'Content here, content here', making it look like readable English.</p>
    <div class="date"><svg width="9" height="9" viewBox="0 0 9 9"><rect x=".5" y="1.5" width="8" height="7" fill="none" stroke="#888"/><line x1=".5" y1="3.5" x2="8.5" y2="3.5" stroke="#888"/></svg>8 December 2013</div>
  </div>
</section>

<footer class="abs footer">
  <div class="fcol" style="left:146px;width:179px">
    <h4>About Us <svg viewBox="0 0 14 14"><circle cx="7" cy="4" r="3" fill="#888"/><path d="M1 14c0-5 12-5 12 0z" fill="#888"/></svg></h4>
    <p>Duis mollis, est non commodo luctus, nisi erat porttitor ligula, eget lacinia odio sem nec elit. Vestibulum id ligula porta felis euismod semper. Integer posuere erat a ante.</p>
    <p>Vestibulum id ligula porta felis euismod semper. Integer posuere erat a ante.</p>
  </div>
  <div class="fcol" style="left:415px;width:180px">
    <h4>Contact Details <svg viewBox="0 0 14 14"><rect x="1" y="3" width="12" height="9" fill="none" stroke="#888"/><path d="M1 3l6 5 6-5" fill="none" stroke="#888"/></svg></h4>
    <p>There are many variations of passages of Lorem Ipsum available, but the majority have suffered alteration.</p>
    <ul class="contact-list">
      <li><svg viewBox="0 0 16 16"><path d="M8 1a5 5 0 0 1 5 5c0 4-5 9-5 9S3 10 3 6a5 5 0 0 1 5-5z" fill="#999"/><circle cx="8" cy="6" r="2" fill="#43484b"/></svg>Eastmere</li>
      <li><svg viewBox="0 0 16 16"><rect x="1" y="3" width="14" height="10" fill="#999"/><path d="M1 3l7 6 7-6" fill="none" stroke="#43484b"/></svg>info@hartwellhire.com</li>
      <li><svg viewBox="0 0 16 16"><path d="M3 1c1 0 3 3 3 4s-1 1-1 2 3 4 4 4 1-1 2-1 4 2 4 3-1 2-3 2C6 15 1 10 1 4c0-2 1-3 2-3z" fill="#999"/></svg>890-09880-41273</li>
    </ul>
  </div>
  <div class="fcol" style="left:683px;top:43px;width:253px">
    <h4>Newsletter Signup <svg viewBox="0 0 14 14"><circle cx="3" cy="11" r="1.6" fill="#888"/><path d="M2 6a6 6 0 0 1 6 6M2 2a10 10 0 0 1 10 10" fill="none" stroke="#888" stroke-width="1.6"/></svg></h4>
    <p style="color:#c7cbcd">By subscribing to our mailing list you will get the latest news from us.</p>
    <div class="signup"><div class="field"></div><div class="go">Subscribe</div></div>
    <div class="get-social">Get Social</div>
    <div class="social-foot"><div class="sq"></div><div class="sq"></div><div class="sq"></div><div class="sq"></div></div>
  </div>
</footer>

<div class="abs bar">
  <div class="copy">Copyright 2014 © CompanyName - All Rights Reserved</div>
  <div class="links"><span>Site Map</span><span>•</span><span>Privacy Policy</span></div>
</div>
</body>
</html>
```